Investment Memorandum Document

IM for Harbourline Lending Fund - is the document that needs work

Make sure it is all done in MS WORD so that i or lawyers can edit some words if required

the IM is NOT final but its 95% of the way there. Maybe a few more pages and wording changes - but that is something i can do i guess or you can easier adjust

Just to typeset and pretty it all up - a few sample finished products have been uploaded for reference.

QOR IM is the one i like - but feel free to show off your skills

put 1.2 to 1.8 all in contrasting row tables

Target Market(s)

Individual and Institutional investors with money

Industry/Entity Type

Investment Banking

Colors

Designer to choose colors to be used in the design.

Requirements
Must have
• clear professional layout and easy on the eye
• https://www.filecrate-example.net/sh/58k3p71zqx4mwtb/BBDrqLwZmUPxTvnQAHMDE42Kb?dl=0
• use the link above for high res images
Nice to have
• pictures and graphics
Should not have
• cartoons

```html
<!DOCTYPE html>
<html lang="en">
<head>
<meta charset="utf-8">
<title>Harbourline Diversified Commercial Income Fund – Information Memorandum</title>
<link rel="stylesheet" href="https://fonts.googleapis.com/css2?family=Open+Sans:ital,wght@0,400;0,600;0,700;1,400&display=swap">
<style>
:root{
  --bg:#8d8d8d;
  --paper:#ffffff;
  --ink:#3a3a3a;
  --muted:#6b6b6b;
  --blue:#2f8fd3;
  --tab:#5aa0dc;
  --table:#cfe2f5;
  --rule:#b9cde0;
  --gold:#c49a52;
}
*{box-sizing:border-box}
html,body{margin:0;padding:0;overflow:hidden}
body{background:var(--bg);font-family:'Open Sans',sans-serif}
.canvas{position:relative;width:1200px;height:1200px;overflow:hidden;background:var(--bg)}
.page{position:absolute;background:var(--paper);color:var(--ink);overflow:hidden;box-shadow:0 1px 4px rgba(0,0,0,.35)}
.mark{position:absolute;top:20px;right:20px;display:flex;align-items:center;gap:2px;font-size:5px;font-weight:600;color:var(--gold)}
.mark i{display:block;width:5px;height:5px;background:var(--gold)}
.folio{position:absolute;right:0;bottom:13px;display:flex;align-items:center;gap:8px;font-size:3.2px;font-style:italic;color:var(--muted)}
.folio .tab{width:52px;height:7px;background:var(--tab);color:#fff;font-style:normal;font-size:3.4px;padding-left:4px;line-height:7px}
.photo{position:absolute}
.txt{position:absolute}
.p{font-size:3.3px;line-height:1.38;margin:0 0 2.6px;text-align:justify}
.h-blue{color:var(--blue);font-weight:600;margin:0}
.h-sub{font-size:3.6px;color:var(--blue);font-weight:600;margin:4px 0 2px}
.h-under{font-size:3.4px;font-weight:700;text-decoration:underline;font-style:italic;margin:3px 0 2px}
.role{font-size:3.3px;font-style:italic;margin:3px 0 1px}
/* cover */
.cover{left:206px;top:14px;width:256px;height:356px}
.cover .photo{inset:0;background:linear-gradient(160deg,#8cbde2 0%,#4f86b8 38%,#2a5685 65%,#18355a 100%)}
.cover-brand{position:absolute;left:30px;top:48px;display:flex;align-items:center;gap:5px;color:#f1dcae;font-size:18px;letter-spacing:3px;font-weight:400}
.cover-brand i{display:block;width:16px;height:16px;background:#d8b878}
.cover-brand small{position:absolute;left:26px;top:22px;font-size:4.5px;letter-spacing:3.5px;color:#e9e4d6;white-space:nowrap}
.cover-title{position:absolute;left:26px;top:95px;color:#fff;font-size:8.2px;font-weight:600;line-height:1.3}
.cover-roles{position:absolute;right:12px;top:286px;text-align:right;color:#fff;line-height:1.2}
.cover-roles b{display:block;font-size:8px;font-weight:600}
.cover-roles span{display:block;font-size:6px;margin-bottom:8px}
/* contents */
.contents-title{position:absolute;left:26px;top:33px;font-size:5.5px;color:var(--blue);font-weight:600}
.toc{position:absolute;left:55px;top:80px;width:155px;font-size:3.6px;font-variant:small-caps;list-style:none;margin:0;padding:0}
.toc li{display:flex;line-height:8.8px}
.toc .n{width:22px}
.toc .t{flex:1}
.toc .pg{width:8px;text-align:right}
/* data tables */
.facts{width:100%;border-collapse:collapse;font-size:3.3px}
.facts td{padding:1.5px 0;border-bottom:.5px solid var(--rule);vertical-align:top}
.facts td:last-child{width:38%}
.proj{position:absolute;display:flex;gap:8px}
.proj .thumb{flex:none}
.proj .info{flex:1}
.proj .name{font-size:3.4px;font-weight:700;text-decoration:underline;margin:0 0 2px}
.proj .addr{font-size:3.3px;margin:0 0 2px;padding-bottom:2px;border-bottom:.5px solid var(--rule)}
.proj .desc{font-size:3.3px;line-height:1.35;margin:0 0 2px;padding-bottom:2px;border-bottom:.5px solid var(--rule)}
.label-it{font-size:3.4px;font-style:italic;text-decoration:underline;position:absolute}
.terms{position:absolute;left:40px;top:34px;width:222px;height:117px;background:var(--table);font-size:3.3px;padding:4px 4px}
.terms td{vertical-align:top;padding:1px 2px}
.terms p{margin:0 0 2.2px;line-height:1.35;text-align:justify}
.num-list{margin:0;padding:0;list-style:none}
.num-list li{display:flex;gap:5px;font-size:3.3px;line-height:1.38;margin-bottom:2px;text-align:justify}
.sec{display:flex;gap:10px;font-size:3.4px;color:var(--blue);font-weight:600;margin:3px 0 1px}
</style>
</head>
<body>
<div class="canvas">

  <!-- Cover -->
  <section class="page cover">
    <div class="photo" role="img" aria-label="Upward view of glass office towers in blue tones"></div>
    <div class="cover-brand"><i></i>HARBOURLINE<small>ASSET MANAGEMENT</small></div>
    <div class="cover-title">Diversified Commercial Income Fund<br>Information Memorandum</div>
    <div class="cover-roles">
      <b>Investment Manager</b><span>Harbourline Asset Management Pty Ltd</span>
      <b>Trustee</b><span>Meridian Trust and Lending Corporation Pty Ltd</span>
    </div>
  </section>

  <!-- Spread: contents -->
  <section class="page" style="left:482px;top:14px;width:247px;height:358px">
    <div class="mark"><i></i>Harbourline</div>
    <div class="contents-title">CONTENTS</div>
    <ul class="toc">
      <li><span class="t">Message from the Managing Director</span><span class="pg">5</span></li>
      <li><span class="n">1.</span><span class="t">The Fund</span><span class="pg">6</span></li>
      <li><span class="n">2.</span><span class="t">The Loans</span><span class="pg">11</span></li>
      <li><span class="n">3.</span><span class="t">Risks</span><span class="pg">13</span></li>
      <li><span class="n">4.</span><span class="t">Fees and Costs</span><span class="pg">16</span></li>
      <li><span class="n">5.</span><span class="t">Management of the Fund</span><span class="pg">18</span></li>
      <li><span class="n">6.</span><span class="t">Taxation Information</span><span class="pg">22</span></li>
      <li><span class="n">7.</span><span class="t">Additional Information</span><span class="pg">23</span></li>
      <li><span class="n">8.</span><span class="t">Application Process</span><span class="pg">26</span></li>
      <li><span class="n">9.</span><span class="t">Glossary</span><span class="pg">27</span></li>
    </ul>
    <div class="photo" style="left:3px;top:186px;width:242px;height:140px;background:linear-gradient(180deg,#b7cbd9 0%,#8fa6b8 45%,#4b5561 75%,#2d3138 100%)" role="img" aria-label="Rooftop terrace with city skyline at dusk"></div>
    <div class="folio">Harbourline Diversified Commercial Income Fund – Information Memorandum<span class="tab">Page 2</span></div>
  </section>

  <!-- Spread: notice -->
  <section class="page" style="left:729px;top:14px;width:247px;height:358px">
    <div class="mark"><i></i>Harbourline</div>
    <div class="txt" style="left:22px;top:33px;width:210px">
      <p class="h-blue" style="font-size:4.6px;margin-bottom:2px">NOTICE</p>
      <p class="p">This information memorandum is dated and is issued by Meridian Trust and Lending Corporation Pty Ltd, holder of an AFS licence, which is the trustee of the Harbourline Diversified Commercial Income Fund (Fund).</p>
      <p class="p">The purpose of this IM is to provide information for prospective investors to decide whether they wish to invest in the Fund.</p>
      <p class="p">The Trustee has appointed Harbourline Asset Management Pty Ltd as the investment manager of the Fund under the Investment Management Agreement. The Investment Manager is an authorised representative of the Trustee.</p>
      <p class="p">The Fund's trust deed provides for different classes of units. Under the trust deed, the different classes of units may have different rights and obligations. The performance of different classes of units may also differ depending on the investments of that class.</p>
      <p class="h-sub" style="font-size:3.3px">NO DISCLOSURE REQUIRED</p>
      <p class="p">This IM is intended to provide potential investors with information only and does not constitute a product disclosure statement or other disclosure document required by law. This IM has not been lodged with any government body.</p>
      <p class="p">The offer made under this IM is only available to persons who qualify as wholesale clients or sophisticated investors. The Trustee will not issue units in the Fund to a person unless it is satisfied that the person is a qualified investor.</p>
      <p class="h-sub" style="font-size:3.3px">RESTRICTIONS ON DISTRIBUTION</p>
      <p class="p">This IM does not constitute, and may not be used for the purposes of, an offer of units or an invitation to apply to participate in the Fund by any person in any jurisdiction in which such offer or invitation is not authorised, or to any person to whom it is unlawful to make such an offer or invitation.</p>
      <p class="p">No action has been taken to register or qualify interests in the Fund, the invitation to participate in the Fund, or to otherwise permit any public offering of Fund interests in any jurisdiction. It is the responsibility of prospective investors to satisfy themselves as to full compliance with the relevant laws and regulations of any jurisdiction in connection with any application to participate in the Fund.</p>
      <p class="p">By receiving and viewing this IM, the recipient is warranting that they are legally entitled to do so and the securities laws of their relevant jurisdiction do not prohibit them from acquiring interests in the Fund. Further, the persons receiving and viewing this IM warrant that they are qualified investors.</p>
      <p class="p">In particular, this product has not been and will not be registered under any foreign securities act, and may not be offered, sold, delivered or transferred in any other state. Neither this IM, application form or other material relating to this product may be distributed there.</p>
      <p class="p">Accordingly, this IM is not a product disclosure statement and does not contain all of the information that would be included in a regulated disclosure document. The Trustee may in the future take actions to offer interests in other jurisdictions.</p>
      <p class="h-sub" style="font-size:3.3px">NO RESPONSIBILITY FOR CONTENTS OF DOCUMENT</p>
      <p class="p">To the maximum extent permitted by law, none of the Trustee, the Investment Manager, or any of their associates, related parties, directors, officers, employees or advisers makes any recommendation in relation to the Fund, or makes any representation or warranty as to the accuracy, reliability or completeness of the information contained in this IM.</p>
      <p class="p">This IM does not purport to contain all the information that a prospective investor may require in evaluating a possible investment in the Fund. This IM must be read in conjunction with the Fund's trust deed which is available free of charge by contacting the Trustee.</p>
      <p class="h-sub" style="font-size:3.3px">NO DISTRIBUTION</p>
      <p class="p">Distribution of this IM to any person other than the persons receiving a copy of this IM from the Trustee or the Investment Manager is unauthorised. Any photocopying, disclosure or alteration of the contents of this IM is prohibited.</p>
    </div>
    <div class="folio">Harbourline Diversified Commercial Income Fund – Information Memorandum<span class="tab">Page 3</span></div>
  </section>

  <!-- Page 10 -->
  <section class="page" style="left:149px;top:374px;width:283px;height:400px">
    <div class="mark"><i></i>Harbourline</div>
    <div class="terms">
      <table style="border-collapse:collapse;width:100%">
        <tr><td style="width:44px"></td><td><p>Class 2 Loan Units: 10% per annum (before tax, after all fees)</p><p>The Target Return is not guaranteed. The Fund may not be successful in meeting this objective.</p></td></tr>
        <tr><td style="font-weight:700;padding-top:4px">Minimum Initial Investment Amount</td><td style="padding-top:4px">
          <p style="text-decoration:underline">Cash Units</p>
          <p>The minimum initial investment for Cash Units is $100,000 from a Qualifying Investor.</p>
          <p>Following the minimum initial investment, Investors may make further investments in increments of $20,000.</p>
          <p style="text-decoration:underline">Loan Units</p>
          <p>The minimum initial investment for Loan Units is $500,000 from a Qualifying Investor.</p>
          <p>Following the minimum initial investment, Investors may make further investments in increments of $50,000.</p>
          <p>However, the Trustee may accept lower amounts from a Qualifying Investor in its absolute discretion.</p>
        </td></tr>
      </table>
    </div>
    <div class="photo" style="left:0;top:178px;width:283px;height:190px;background:linear-gradient(165deg,#e4e7ec 0%,#c7ccd4 45%,#9b6a4d 78%,#5d3a2a 100%)" role="img" aria-label="Tall residential tower against a cloudy sky"></div>
    <div class="folio">Harbourline Diversified Commercial Income Fund – Information Memorandum<span class="tab">Page 10</span></div>
  </section>

  <!-- Page 12 -->
  <section class="page" style="left:455px;top:374px;width:283px;height:400px">
    <div class="mark"><i></i>Harbourline</div>
    <div class="txt" style="left:40px;top:36px;width:222px">
      <p class="p">The enforcement procedure can involve significant costs, including legal costs and receiver's fees. These costs may be funded as follows:</p>
      <ol class="num-list">
        <li><span>1.</span><span>Paid by the Investment Manager from its own funds. In which case, the Investment Manager will be able to recover these costs from the proceeds received from the Borrower in priority to any payment to Investors.</span></li>
        <li><span>2.</span><span>By the Trustee undertaking a rights offer to raise the capital required. It is likely that any future capital raising undertaken to pay for enforcement expenses would be undertaken at an issue price less than the original issue price of $1 per Unit and will therefore be dilutive. It is important for Investors to understand there is a possibility they may have to contribute further capital to the Fund in the future and if an Investor chooses not to contribute, their proportionate holding in the Fund may be diluted.</span></li>
        <li><span>3.</span><span>Paid by a third party. In which case, any expenses paid plus any amount agreed with the lender (for example, success fees) would be recovered from the proceeds received from the Borrower in priority to any payment to Investors.</span></li>
      </ol>
      <div class="sec" style="margin-left:-13px"><span>2.5</span><span>Investing surplus funds</span></div>
      <p class="p">From time to time the Trustee may have excess capital which is not immediately required or able to be invested in the suitable loans or funds which are being held pending distribution to Investors. In those circumstances the Trustee may invest those funds in cash and cash equivalents (i.e. term deposits offered by ADIs).</p>
    </div>
    <div class="photo" style="left:0;top:178px;width:283px;height:190px;background:linear-gradient(180deg,#a6c2e0 0%,#7d9cbd 40%,#45607f 70%,#23324a 100%)" role="img" aria-label="Rooftop infinity pool overlooking a city observation wheel at dusk"></div>
    <div class="folio">Harbourline Diversified Commercial Income Fund – Information Memorandum<span class="tab">Page 12</span></div>
  </section>

  <!-- Page 17 -->
  <section class="page" style="left:766px;top:374px;width:283px;height:400px">
    <div class="mark"><i></i>Harbourline</div>
    <div class="txt" style="left:27px;top:34px;width:235px">
      <div class="sec"><span>4.3</span><span>Waiver, deferral or rebate of fees</span></div>
      <p class="p" style="margin-left:13px">The Trustee may, in its absolute discretion, accept lower fees and expenses than it is entitled to receive, or may defer payment of those fees and expenses for any time. If payment is deferred, then the fee will accrue until paid. In addition, the Investment Manager or Trustee may waive, negotiate or rebate their fees, for example, in the case of a large investment amount.</p>
      <div class="sec" style="margin-top:5px"><span>4.4</span><span>Referral fees</span></div>
      <p class="p" style="margin-left:13px">The Investment Manager can offer referral fees or rebates at the Investment Manager's sole discretion, provided this is at the Investment Manager's own expense.</p>
    </div>
    <div class="photo" style="left:0;top:178px;width:283px;height:190px;background:linear-gradient(180deg,#cfcac0 0%,#a79f93 40%,#5b554d 75%,#35312d 100%)" role="img" aria-label="Furnished apartment living room with floor to ceiling windows"></div>
    <div class="folio">Harbourline Diversified Commercial Income Fund – Information Memorandum<span class="tab">Page 17</span></div>
  </section>

  <!-- Page 18 -->
  <section class="page" style="left:12px;top:788px;width:283px;height:400px">
    <div class="mark"><i></i>Harbourline</div>
    <div class="txt" style="left:28px;top:36px;width:244px">
      <p class="h-blue" style="font-size:5.6px;margin-bottom:3px">5.&nbsp;&nbsp;&nbsp;Keystone Property Group</p>
      <p class="p">Keystone Property Group (Keystone) is a strategic property investment group headquartered in Central City, with an established a record of success in the property market since 2012. Keystone pursues an integrated approach in which it invests and operates across the lifecycle of high-quality property.</p>
      <p class="p">Its 'buy, build, own' model allows the group to capture multiple revenue streams through the development, funding, ownership and management of prime real estate assets.</p>
      <p class="p">Keystone focuses on high quality, 5-star property, combining the best in design, urban planning and construction and incorporating commercial, retail and residential elements.</p>
      <p class="p">Partnerships with leading international hotel groups such as Aldwyn Hotels and Corvel (recently acquired by Vantis Hotels in 2018) strengthen its capability to pursue this market.</p>
      <p class="p">The group has a current pipeline of projects worth in excess of $1.0 billion in end project value and has plans to invest in broader business opportunities that complement its core real estate operations.</p>
      <p class="h-sub" style="font-size:3.4px">Key Management</p>
      <p class="role">Daniel Hart – Founder &amp; Chief Executive</p>
      <p class="p">Daniel Hart is Central City raised, and has strong connections with regional investors. He has a sound understanding of design, architecture, urban planning and construction, and extensive experience developing projects in a large, complex city environment. Daniel was awarded the National Property Institute 'Young Achiever of the Year' award in 2015. He has grown Keystone from inception into a business with projects in excess of $1.0 billion in end value, as well as stamping his mark on the hotels and hospitality industry.</p>
      <p class="role">Marcus Lin – Chief Financial Officer</p>
      <p class="p">Marcus Lin has a wealth of international experience in financial and risk management, investor relations and compliance. He has worked in financial markets across several regions. A qualified Chartered Accountant, with a core banking background, Marcus carefully identifies opportunities across the property sector with a measured approach to structuring transactions and fulfilling the funding stack from both debt and equity perspectives.</p>
      <p class="h-sub" style="font-size:3.4px">Track Record and Project Pipeline</p>
      <p class="h-under" style="font-style:normal;margin-top:1px">SUCCESSFULLY COMPLETED</p>
    </div>
    <div class="proj" style="left:48px;top:256px;width:224px">
      <div class="thumb photo" style="position:relative;width:88px;height:90px;background:linear-gradient(180deg,#3c4a66 0%,#7a5a4a 60%,#2b2622 100%)" role="img" aria-label="Hotel and apartment building at twilight"></div>
      <div class="info">
        <p class="name">M EASTPORT</p>
        <p class="addr">412 Harbour Street, Eastport</p>
        <p class="desc">Mixed use development comprising 5-star Lakeview Eastport hotel and 186 residential apartments. Hotel retained and subject to a 15-year fixed lease agreement.</p>
        <table class="facts">
          <tr><td>Acquired</td><td>2014</td></tr>
          <tr><td>Completion</td><td>2015</td></tr>
          <tr><td>Project Value</td><td>$150m</td></tr>
          <tr><td>Current Asset Value (hotel only)</td><td>$50m</td></tr>
        </table>
      </div>
    </div>
    <div class="folio">Harbourline Diversified Commercial Income Fund – Information Memorandum<span class="tab">Page 18</span></div>
  </section>

  <!-- Page 19 -->
  <section class="page" style="left:307px;top:788px;width:283px;height:400px">
    <div class="mark"><i></i>Harbourline</div>
    <div class="proj" style="left:35px;top:33px;width:222px">
      <div class="thumb photo" style="position:relative;width:76px;height:92px;background:linear-gradient(180deg,#d5d9de 0%,#8f959c 55%,#44484d 100%)" role="img" aria-label="Curved white apartment tower"></div>
      <div class="info">
        <p class="name">PARKSIDE CRESCENT APARTMENTS</p>
        <p class="addr">18-22 Wren Street, Riverside</p>
        <p class="desc">JV development with NPI acting as equity finance partner with 33% ownership. All 238 residential apartments to be divested on completion.</p>
        <table class="facts">
          <tr><td>Acquired</td><td>2014</td></tr>
          <tr><td>Completion</td><td>2018</td></tr>
          <tr><td>Project Value</td><td>$142m</td></tr>
        </table>
      </div>
    </div>
    <p class="label-it" style="left:28px;top:177px;margin:0">CURRENT PROJECTS</p>
    <div class="proj" style="left:35px;top:190px;width:222px">
      <div class="thumb photo" style="position:relative;width:94px;height:94px;background:linear-gradient(180deg,#9cb0c8 0%,#c6c9cc 45%,#585a5e 100%)" role="img" aria-label="Render of hotel and residential towers"></div>
      <div class="info">
        <p class="name">EASTPORT RESIDENCES &amp; ALDWYN HOTEL</p>
        <p class="addr">5-41 Quayline Way, Eastport</p>
        <p class="desc">Mixed use development comprising 5-star Aldwyn Hotel and 88 residential apartments. Hotel to be retained and apartments to be divested on completion.</p>
        <table class="facts">
          <tr><td>Acquired</td><td>2014</td></tr>
          <tr><td>Completion</td><td>2020</td></tr>
          <tr><td>Project Value</td><td>$237m</td></tr>
          <tr><td>Anticipated Retained Asset Value at completion (hotel only)</td><td>$152m</td></tr>
        </table>
      </div>
    </div>
    <div class="proj" style="left:35px;top:282px;width:222px">
      <div class="thumb photo" style="position:relative;width:94px;height:96px;background:linear-gradient(180deg,#b9c7d6 0%,#8d98a5 50%,#4b4f56 100%)" role="img" aria-label="Render of faceted glass hotel building"></div>
      <div class="info">
        <p class="name">RIVERSIDE QUARTER &amp; ALDWYN SELECT HOTELS</p>
        <p class="addr">140-146 Calder Road, Riverside</p>
        <p class="desc">Mixed use development comprising 5-star Aldwyn Select Hotel and 111 residential apartments. Hotel to be retained and apartments to be divested on completion.</p>
        <table class="facts">
          <tr><td>Acquired</td><td>2017</td></tr>
          <tr><td>Completion</td><td>2021</td></tr>
          <tr><td>Project Value</td><td>$224m</td></tr>
          <tr><td>Anticipated Retained Asset Value at completion (hotel only)</td><td>$129m</td></tr>
        </table>
      </div>
    </div>
    <div class="folio">Harbourline Diversified Commercial Income Fund – Information Memorandum<span class="tab">Page 19</span></div>
  </section>

  <!-- Page 20 -->
  <section class="page" style="left:602px;top:788px;width:284px;height:400px">
    <div class="mark"><i></i>Harbourline</div>
    <p class="label-it" style="left:28px;top:35px;margin:0">FUTURE PROJECTS</p>
    <div class="proj" style="left:31px;top:47px;width:225px">
      <div class="thumb photo" style="position:relative;width:94px;height:96px;background:linear-gradient(180deg,#aab6c2 0%,#7d8893 50%,#3f454c 100%)" role="img" aria-label="Render of twin glass towers on the waterfront"></div>
      <div class="info">
        <p class="name">EASTPORT RESIDENCES &amp; ALDWYN HOTEL</p>
        <p class="addr">5-41 Quayline Way, Eastport</p>
        <p class="desc">Mixed use development comprising commercial spaces and residential apartments. Commercial to be retained and apartments to be divested on completion.</p>
        <table class="facts">
          <tr><td>Acquired</td><td>2014</td></tr>
          <tr><td>Completion</td><td>2020</td></tr>
          <tr><td>Project Value</td><td>$292-323m</td></tr>
          <tr><td>Anticipated Retained Asset Value at completion (hotel only)</td><td>$195-215m</td></tr>
          <tr><td>Current Site Value</td><td>$33m</td></tr>
        </table>
      </div>
    </div>
    <div class="proj" style="left:31px;top:168px;width:225px">
      <div class="thumb photo" style="position:relative;width:94px;height:94px;background:linear-gradient(180deg,#9fb3c9 0%,#c9b8a2 50%,#4f4a45 100%)" role="img" aria-label="Render of slim hotel tower among city buildings"></div>
      <div class="info">
        <p class="name">GRANT STREET</p>
        <p class="addr">88-102 Grant Street, Central City</p>
        <p class="desc">Mixed use development comprising a 5-star hotel and residential apartments. Hotel to be retained and apartments to be divested on completion. Current rental income of $1.3m p.a.</p>
        <table class="facts">
          <tr><td>Acquired</td><td>2016</td></tr>
          <tr><td>Completion</td><td>2021</td></tr>
          <tr><td>Project Value</td><td>$400-442m</td></tr>
          <tr><td>Anticipated Retained Asset Value at completion (hotel only)</td><td>$274-303m</td></tr>
          <tr><td>Current Site Value</td><td>$53m</td></tr>
        </table>
      </div>
    </div>
    <div class="folio">Harbourline Diversified Commercial Income Fund – Information Memorandum<span class="tab">Page 20</span></div>
  </section>

  <!-- Page 26 -->
  <section class="page" style="left:897px;top:788px;width:283px;height:400px">
    <div class="mark"><i></i>Harbourline</div>
    <div class="txt" style="left:28px;top:36px;width:236px">
      <p class="h-blue" style="font-size:5.6px;margin-bottom:3px">9.&nbsp;&nbsp;&nbsp;Application Process</p>
      <p class="p">After reviewing this IM, Investors can invest in Cash Units or Loan Units by completing the Application Form and paying their application money. Payments must be made via electronic funds transfer (bank transfer) or bank cheque.</p>
      <p class="p">Once the completed Application Form and application money is received by the Trustee and the Trustee accepts the application, Investors will be issued with Units. Units will be issued within 5 Business Days of the end of each calendar month in which the completed Application Form and corresponding application money is received, or at any other time at the Trustee's absolute discretion.</p>
      <p class="p">Application monies are held in the Fund's Application Account prior to being allocated to Cash Units. Please note that no interest will be earned by Investors on monies that are held in the Application Account.</p>
    </div>
    <div class="photo" style="left:0;top:192px;width:283px;height:176px;background:linear-gradient(180deg,#6f8fc2 0%,#3d5f98 45%,#25406e 75%,#152645 100%)" role="img" aria-label="Rooftop pool overlooking the city skyline at twilight"></div>
    <div class="folio">Harbourline Diversified Commercial Income Fund – Information Memorandum<span class="tab">Page 26</span></div>
  </section>

</div>
</body>
</html>
```